Tidewell Pest Solutions *

I work as a pest control technician with other company. Now I want to start my own business.

So I want a new logo and business card design (both side of the card).

Colour combination I like Green/Red/white.

On card may have some sort of insect/ but not sure.

Target Market(s)

Anyone in Sydney. There is no specific target.

Industry/Entity Type

Business

Logo Text

Tidewell Pest Solutions

```html
<!DOCTYPE html>
<html lang="en">
<head>
<meta charset="utf-8">
<title>Tidewell Pest Solutions – Business Card</title>
<link rel="stylesheet" href="https://fonts.googleapis.com/css2?family=Arimo:wght@400;700&display=swap">
<style>
  :root {
    --backdrop: #9b9b9b;
    --card-light: #ffffff;
    --card-dark: #3a3536;
    --brand-red: #d40000;
    --ink: #2b2b2b;
    --rule: #8a8a8a;
    --mark-ring: #3a3536;
    --mark-ring-light: #ffffff;
  }
  * { margin: 0; padding: 0; box-sizing: border-box; }
  html, body {
    width: 1200px; height: 900px; overflow: hidden;
    background: var(--backdrop);
    font-family: "Arimo", Arial, sans-serif;
  }
  .canvas { position: relative; width: 1200px; height: 900px; }

  .card { position: absolute; top: 306px; width: 439px; height: 271px; border-radius: 10px; }
  .card--front { left: 150px; background: var(--card-light); }
  .card--back { left: 610px; background: var(--card-dark); }

  /* front: brand mark */
  .brand-mark {
    position: absolute; left: 45px; top: 77px;
    width: 128px; height: 128px; border-radius: 50%;
    border: 5px solid var(--mark-ring);
    display: flex; align-items: center; justify-content: center;
    text-align: center;
  }
  .brand-mark__name {
    color: var(--brand-red); font-weight: 700; font-size: 15px;
    line-height: 1.2; text-transform: uppercase; letter-spacing: 0.5px;
  }

  .divider { position: absolute; left: 207px; top: 75px; width: 1px; height: 122px; background: var(--rule); }

  .contact { position: absolute; left: 223px; top: 70px; color: var(--ink); }
  .contact__name { color: var(--brand-red); font-weight: 700; font-size: 16px; line-height: 19px; text-transform: uppercase; }
  .contact__role { font-size: 13px; line-height: 15px; margin-bottom: 8px; }
  .contact__list { list-style: none; margin-bottom: 6px; }
  .contact__item { display: flex; align-items: center; gap: 2px; font-size: 13px; line-height: 16px; }
  .contact__icon { width: 13px; height: 13px; flex: none; }
  .contact__address { font-size: 13px; line-height: 16px; font-style: normal; }

  /* back: wordmark */
  .wordmark {
    position: absolute; left: 103px; top: 98px;
    display: flex; align-items: center; gap: 27px;
  }
  .wordmark__dot { width: 63px; height: 63px; border-radius: 50%; border: 4px solid var(--mark-ring-light); flex: none; }
  .wordmark__name {
    color: var(--brand-red); font-weight: 700; text-transform: uppercase;
    display: flex; flex-direction: column;
  }
  .wordmark__line--main { font-size: 25px; line-height: 28px; letter-spacing: -0.5px; }
  .wordmark__line--sub { font-size: 13px; line-height: 16px; letter-spacing: 5.6px; }
</style>
</head>
<body>
<main class="canvas">
  <section class="card card--front" aria-label="Business card front">
    <div class="brand-mark">
      <span class="brand-mark__name">Tidewell<br>Pest<br>Solutions</span>
    </div>
    <div class="divider"></div>
    <div class="contact">
      <h1 class="contact__name">Marcus Hale</h1>
      <p class="contact__role">Managing Director</p>
      <ul class="contact__list">
        <li class="contact__item">
          <svg class="contact__icon" viewBox="0 0 14 14" aria-hidden="true"><circle cx="7" cy="7" r="6" fill="none" stroke="var(--brand-red)" stroke-width="1.6"/><path d="M4.6 3.8l1.3 1.4-.7 1c.5 1 1.2 1.7 2.2 2.2l1-.7 1.4 1.3-.9 1.2C6.3 9.9 4.1 7.7 3.8 5z" fill="var(--brand-red)"/></svg>
          <span>444 555 6688</span>
        </li>
        <li class="contact__item">
          <svg class="contact__icon" viewBox="0 0 14 14" aria-hidden="true"><circle cx="7" cy="7" r="7" fill="var(--brand-red)"/><rect x="3.5" y="4.8" width="7" height="4.6" fill="#fff"/><path d="M3.5 4.8L7 7.4l3.5-2.6" fill="none" stroke="var(--brand-red)" stroke-width="0.9"/></svg>
          <span>info@youremail.com</span>
        </li>
        <li class="contact__item">
          <svg class="contact__icon" viewBox="0 0 14 14" aria-hidden="true"><circle cx="7" cy="7" r="7" fill="var(--brand-red)"/><circle cx="7" cy="7" r="3.6" fill="none" stroke="#fff" stroke-width="1.2"/><path d="M3.4 7h7.2M7 3.4c-1.5 2-1.5 5.2 0 7.2M7 3.4c1.5 2 1.5 5.2 0 7.2" fill="none" stroke="#fff" stroke-width="0.8"/></svg>
          <span>www.websitename.com</span>
        </li>
      </ul>
      <address class="contact__address">421, Address line here<br>Country Name,45452</address>
    </div>
  </section>

  <section class="card card--back" aria-label="Business card back">
    <div class="wordmark">
      <span class="wordmark__dot"></span>
      <span class="wordmark__name">
        <span class="wordmark__line--main">Tidewell Pest</span>
        <span class="wordmark__line--sub">Solutions</span>
      </span>
    </div>
  </section>
</main>
</body>
</html>
```